New Packaging Design Project for Matcha Green Tea

**I've added an image called 'Sizing example', this is to show you the size of the label compared to the pack. Currently we are using full size labels for the pack and they are too difficult to apply.
Hi. I need a new label creating for a 100g pack of stunning organic premium grade Matcha tea.
The label needs to be 69mm by 88.9mm on the finished product and will be placed on a foil pack which is somewhat larger than the label.
Needs to include the text:
"Matcha Green Tea"
"Organic Japanese Premium Grade"
"Perfect for drinking, blending and baking"
"100g"
Attaching our logo and the KPV certification which both need to be on the label.
You can see our other products at www.leafhollowco.co.uk
You key with this product is that we need it to stand out on Bazolia. There are many, many other Matcha products in foil packs, so this needs to be a bold and fresh design. My suggestion is to test the design by editing it into a screenshot of the Bazolia search page for matcha tea to see if it stands out.
Target Market(s)
Affluent health conscious individuals. Those with busy life, such as executives or parents,. Those with an active life, such as triathletes, yoga, cyclists. Those with a aspirational life, i.e. they want to have quality in their life and they aspire to have the latest trends.
Requirements
Must have
- Stand out design. Clear, clean, crisp.
- Our green colour is #63A802 / 99 / 168 / 2. C41, M0, Y99, K34
- We also sometimes use #144400- R: 20 G: 68 B: 0
Nice to have
- Could either show how the product is used - i.e. lifestyle or just show the quality of the product.
- Could show the product in a ceremonial style bowl, a matcha latte or being blended or used for baking. Could even show all of these, so long as it doesn't look 'busy'.
Should not have
- Clutter, too many things going on.

```html
<!DOCTYPE html>
<html lang="en">
<head>
<meta charset="utf-8">
<title>Leafhollow Matcha Green Tea – 100g Label</title>
<link rel="stylesheet" href="https://fonts.googleapis.com/css2?family=Advent+Pro:wght@300&family=Comfortaa:wght@400&family=Roboto:wght@500&display=swap">
<style>
  :root {
    --brand-green: #63a802;
    --deep-green: #144400;
    --ink: #333333;
    --label-white: #ffffff;
    --backdrop: #f3f3f3;
    --cup-red: #e0231c;
    --cup-red-dark: #c41810;
    --powder-green: #7fa83a;
  }
  * { margin: 0; padding: 0; box-sizing: border-box; }
  html, body { width: 1000px; height: 1200px; overflow: hidden; background: var(--backdrop); }
  .canvas { position: relative; width: 1000px; height: 1200px; }
  .label-frame, .product-photo { position: absolute; left: 0; top: 0; }
  .label-frame { z-index: 1; }
  .product-photo { z-index: 2; }
  .label-text { position: absolute; z-index: 3; line-height: 1; }
  .brand-name {
    left: 0; width: 1000px; top: 214px; text-align: center;
    font-family: "Comfortaa", sans-serif; font-size: 38px; color: var(--brand-green);
  }
  .grade-line {
    left: 0; width: 1000px; top: 313px; text-align: center;
    font-family: "Roboto", sans-serif; font-weight: 500; font-size: 19px; color: var(--ink);
  }
  .product-title {
    left: 0; width: 1000px; top: 345px; text-align: center;
    font-family: "Advent Pro", sans-serif; font-weight: 300; font-size: 112px;
    letter-spacing: 2px; color: var(--brand-green);
  }
  .product-subtitle {
    right: 322px; top: 458px;
    font-family: "Roboto", sans-serif; font-weight: 500; font-size: 27px; color: var(--brand-green);
  }
  .usage-list {
    right: 310px; top: 520px; text-align: right; list-style: none;
    font-family: "Comfortaa", sans-serif; font-size: 28px; line-height: 38px; color: var(--ink);
  }
  .cert-badge {
    position: absolute; z-index: 3; left: 250px; top: 866px; width: 44px; height: 44px;
    border: 3px solid var(--deep-green); border-radius: 50%;
  }
  .net-weight {
    left: 415px; width: 200px; top: 912px; text-align: center;
    font-family: "Roboto", sans-serif; font-weight: 500; font-size: 36px; color: var(--label-white);
  }
</style>
</head>
<body>
<main class="canvas">
  <svg class="label-frame" width="1000" height="1200" viewBox="0 0 1000 1200" aria-hidden="true">
    <path d="M230 246 A18 18 0 0 0 248 228 L279 228 C279 190 330 175 380 168 Q500 150 620 168 C670 175 720 190 720 228 L756 228 A18 18 0 0 0 774 246 L774 948 A18 18 0 0 0 756 966 L706 966 C706 1010 660 1030 620 1036 Q500 1050 380 1036 C340 1030 292 1010 292 966 L248 966 A18 18 0 0 0 230 948 Z"
          fill="var(--label-white)" stroke="var(--brand-green)" stroke-width="8" stroke-linejoin="round"/>
  </svg>

  <svg class="product-photo" width="1000" height="1200" viewBox="0 0 1000 1200" role="img"
       aria-label="Photo of matcha powder with a bamboo whisk and a matcha latte in a red cup and saucer">
    <defs>
      <radialGradient id="powder" cx="0.5" cy="0.5" r="0.5">
        <stop offset="0" stop-color="var(--powder-green)"/>
        <stop offset="0.7" stop-color="var(--powder-green)" stop-opacity="0.6"/>
        <stop offset="1" stop-color="var(--powder-green)" stop-opacity="0"/>
      </radialGradient>
      <radialGradient id="cup" cx="0.5" cy="0.5" r="0.5">
        <stop offset="0" stop-color="#b8c77a"/>
        <stop offset="0.42" stop-color="#c9d48f"/>
        <stop offset="0.5" stop-color="#ffffff"/>
        <stop offset="0.56" stop-color="var(--cup-red)"/>
        <stop offset="1" stop-color="var(--cup-red-dark)"/>
      </radialGradient>
    </defs>
    <ellipse cx="368" cy="640" rx="125" ry="115" fill="url(#powder)"/>
    <circle cx="515" cy="825" r="128" fill="url(#cup)"/>
  </svg>

  <p class="label-text brand-name">Leafhollow</p>
  <p class="label-text grade-line">Organic Japanese Premium Grade</p>
  <h1 class="label-text product-title">MATCHA</h1>
  <p class="label-text product-subtitle">Green Tea</p>
  <ul class="label-text usage-list">
    <li>Perfect for</li>
    <li>drinking</li>
    <li>blending</li>
    <li>and baking</li>
  </ul>
  <div class="cert-badge" role="img" aria-label="Organic certification badge"></div>
  <p class="label-text net-weight">100g</p>
</main>
</body>
</html>
```